HIgh-end jewelry designer needs a business card design

I need a business card design for the ecclectic & rather expensive jewelry designs. My approach to my work is to combine very old jewelry offset with contemporary items. I enjoy the idea of legacy as well as repurposing finely crafted items that are not possible to create any longer. My desire is to celebrate the past in a contemporary & funky way. The name of my business is MERIVALE. I see my business card design as simple & yet enigmatic as possible. In the end... clean, simple & understated is the look I am after. Thank you for your consideration...

Target Market(s)

I will use this business card for the trade as well as customers

Industry/Entity Type

Business

Contact Information for Business Card

Corinne Halvard Owner/Designer 555-274-8163

Requirements
Must have
• Clean & simple sophisticated design using the word "Merivalle" as the logo. I like the idea of a play on the word itself, perhaps even using different fonts (i.e.: a bold helvetica combined with a lovely script). I'm afraid to say more because I don't want to limit creative input. Gosh, sometimes it's ok to break the rules!
Nice to have
• In my mind, I have imagined this business card to be simple, using my company name "Merivale" in a playful yet sophisticated manner. I believe that doing something beautifully simple can be a true challenge. I have imagined something with just black & white, however I am open to ideas... after all that's why I'm here!
Should not have
• As Mozart once said... "It has too many notes!" I know I'm being silly, but I don't want it to be complicated or overly ornate.

```html
<!DOCTYPE html>
<html lang="en">
<head>
<meta charset="utf-8">
<title>Merivale — Business Card</title>
<link rel="stylesheet" href="https://fonts.googleapis.com/css2?family=Amatic+SC:wght@400;700&display=swap">
<style>
  :root {
    --backdrop: #e4e2de;
    --card-black: #0d0d0d;
    --ink-cream: #f1ebe0;
    --ink-muted: #b8b2a8;
    --pattern-tone: #3a3835;
    --pattern-tone-light: #4a4743;
  }
  * { box-sizing: border-box; margin: 0; padding: 0; }
  html, body {
    width: 1200px;
    height: 800px;
    overflow: hidden;
    background: var(--backdrop);
  }
  .business-card {
    position: absolute;
    left: 110px;
    top: 120px;
    width: 980px;
    height: 560px;
    background: var(--card-black);
    overflow: hidden;
    font-family: "Amatic SC", "Arial Narrow", sans-serif;
    color: var(--ink-cream);
  }
  .pattern-band {
    position: absolute;
    background: linear-gradient(90deg, var(--pattern-tone), var(--pattern-tone-light), var(--pattern-tone));
  }
  .pattern-band--top { left: 0; right: 0; top: 18px; height: 126px; }
  .pattern-band--middle { left: 0; right: 0; top: 298px; height: 32px; }
  .pattern-band--bottom { left: 60px; right: 30px; top: 482px; height: 48px; }
  .rule {
    position: absolute;
    left: 0;
    right: 0;
    height: 3px;
    background: var(--ink-cream);
  }
  .rule--upper { top: 150px; }
  .rule--lower { top: 340px; }
  .brand-name {
    position: absolute;
    top: 168px;
    left: 0;
    right: 0;
    text-align: center;
    font-weight: 700;
    font-size: 118px;
    letter-spacing: 6px;
    line-height: 1;
  }
  .contact-name {
    position: absolute;
    left: 60px;
    top: 362px;
    font-weight: 700;
    font-size: 62px;
    letter-spacing: 2px;
    line-height: 1;
  }
  .contact-role {
    position: absolute;
    left: 60px;
    top: 432px;
    font-weight: 400;
    font-size: 40px;
    letter-spacing: 2px;
    line-height: 1;
    color: var(--ink-muted);
  }
  .contact-phone {
    position: absolute;
    right: 70px;
    top: 356px;
    font-weight: 400;
    font-size: 42px;
    letter-spacing: 2px;
    line-height: 1;
    color: var(--ink-muted);
  }
</style>
</head>
<body>
  <main class="business-card">
    <div class="pattern-band pattern-band--top" role="img" aria-label="Hand-drawn layered zigzag border pattern in cream on black"></div>
    <div class="rule rule--upper"></div>
    <h1 class="brand-name">MERIVALE</h1>
    <div class="pattern-band pattern-band--middle" role="img" aria-label="Row of small hand-drawn chevron marks in cream"></div>
    <div class="rule rule--lower"></div>
    <p class="contact-phone">555-274-8163</p>
    <p class="contact-name">CORINNE HALVARD</p>
    <p class="contact-role">OWNER / DESIGNER</p>
    <div class="pattern-band pattern-band--bottom" role="img" aria-label="Single hand-drawn zigzag line border in cream"></div>
  </main>
</body>
</html>
```